Business Card Design

I would like a logo created for the top left corner of the card please. I would like a checkerboard in a dark navy with the edges fading out and one random bright orange square.
Updates

I have attached some further notes and a really rough sketch of what I am after.  Thank you. :)

Target Market(s)

Construction, mining, mechanical

Industry/Entity Type

Business

Contact Information for Business Card

Korvane Works Pty Ltd, Glen Hadwick, P. 0418365072, F. 0736209158, E.glen@korvaneworks.com.au, PO Box 87 YARRAWONGA Q 4581, ABN 53209874611

Font styles to use
Sans Serif

Requirements
Must have
• Really Dark Navy
Really bright Orange

```html
<!DOCTYPE html>
<html lang="en">
<head>
<meta charset="utf-8">
<title>Korvane Works Pty Ltd – Business Card</title>
<link rel="stylesheet" href="https://fonts.googleapis.com/css2?family=Archivo:wght@400;500;600&display=swap">
<style>
  :root {
    --navy: #262262;
    --navy-mark: #2b3590;
    --orange: #f15a29;
    --card: #ffffff;
    --backdrop: #c3d0da;
  }
  html, body {
    margin: 0;
    padding: 0;
    width: 1200px;
    height: 1000px;
    overflow: hidden;
    background: var(--backdrop);
    font-family: "Archivo", Arial, sans-serif;
  }
  .card {
    position: absolute;
    left: 160px;
    top: 229px;
    width: 880px;
    height: 542px;
    background: var(--card);
    box-shadow: 6px 6px 8px rgba(0, 0, 0, 0.35);
  }
  .card__edge {
    position: absolute;
    top: 0;
    right: 0;
    width: 32px;
    height: 100%;
    background: var(--orange);
  }
  .brand-mark {
    position: absolute;
    left: 34px;
    top: 29px;
    width: 108px;
    height: 108px;
    background: var(--navy-mark);
  }
  .company-name {
    position: absolute;
    left: 165px;
    top: 58px;
    margin: 0;
    font-size: 39px;
    font-weight: 600;
    color: var(--orange);
    letter-spacing: 0.2px;
    white-space: nowrap;
  }
  .person {
    position: absolute;
    left: 166px;
    top: 133px;
    margin: 0;
    font-size: 34px;
    font-weight: 600;
    color: var(--navy);
  }
  .direct-line {
    position: absolute;
    left: 163px;
    top: 181px;
    margin: 0;
    font-size: 34px;
    color: var(--orange);
  }
  .direct-line .label { font-weight: 600; margin-right: 18px; }
  .contact-list {
    position: absolute;
    left: 0;
    top: 316px;
    margin: 0;
    display: grid;
    grid-template-columns: 74px auto;
    column-gap: 24px;
    row-gap: 7px;
    font-size: 29px;
    line-height: 37px;
    color: var(--navy);
  }
  .contact-list dt {
    text-align: right;
    font-weight: 600;
    color: var(--orange);
  }
  .contact-list dd { margin: 0; white-space: nowrap; }
  .contact-list .address { margin-top: 6px; line-height: 34px; }
</style>
</head>
<body>
  <article class="card">
    <div class="brand-mark" aria-hidden="true"></div>
    <h1 class="company-name">KORVANE WORKS PTY LTD</h1>
    <p class="person">Glen Hadwick</p>
    <p class="direct-line"><span class="label">P:</span>0418365072</p>
    <dl class="contact-list">
      <dt>F:</dt><dd>0736209158</dd>
      <dt>E:</dt><dd>glen@korvaneworks.com.au</dd>
      <dt>W:</dt><dd>www.korvaneworks.com.au</dd>
      <dt class="address">A:</dt><dd class="address">PO Box 87&nbsp; YARRAWONGA&nbsp; Q 4581<br>ABN 532 09874611</dd>
    </dl>
    <div class="card__edge"></div>
  </article>
</body>
</html>
```